Transportation Brokerage and Freight Forwarder

We need a plain square mark company page to attract potential customers (Shippers) and potential Drivers (Truck Drivers) for our business. We provide nationwide shipping services for contract customers in all areas of the Supply Chain LTL (Less than Truck Load), TL (Truck Load) Sea Freight (Ocean Vessels), Air Freight (Air Cargo), Container Freight, Rail Freight (Trains). We are also a Transportation Consulting Company as well helping clients to create Shipping solutions to improve there shipping capacity or cut cost by suggesting different modes of transport based upon their needs.

We have over 50+ years experience in the industry to include Driving (myself and my partner still hold CDL licenses currently), Dispatching Management, Operations Management and former Transport Executives, we are also doing work in other countries with our strategic partners in the form of Freight forwarding services that we offer.

Target Market(s)

The Transport and Shipping community in the U.S., Truck, Train, Ship, Plane & Container

Font styles to use
Serif
Sans Serif

Colors

Designer to choose colors to be used in the design.

Requirements
Must have
• Targeted services we provide (use our website for ideas) www.vrnhtp.com. We want to get the name out there, use stock photos from the Logistics industry
Nice to have
• Appealing attraction to the page itself, want to draw views
Should not have
• No overkill of information

```html
<!DOCTYPE html>
<html lang="en">
<head>
<meta charset="utf-8">
<title>Cargo Bridge Partners – Company Page</title>
<link href="https://fonts.googleapis.com/css2?family=Lato:wght@400;700&family=Montserrat:wght@500;600;700&family=Noto+Serif:wght@400&family=Open+Sans:wght@400;600&display=swap" rel="stylesheet">
<style>
:root{
  --bar:#4267b2;
  --page-bg:#e9ebee;
  --card:#ffffff;
  --line:#dddfe2;
  --navy:#0d2f63;
  --navy-deep:#0a2a5a;
  --sky:#5bb6dc;
  --ink:#1d2129;
  --muted:#7f7f7f;
  --grey-text:#606770;
  --cta:#4080ff;
  --verified:#3b8ff0;
}
*{box-sizing:border-box;margin:0;padding:0}
html,body{width:1200px;height:585px;overflow:hidden}
body{background:var(--page-bg);font-family:"Open Sans",Arial,sans-serif;position:relative;color:var(--ink)}
.abs{position:absolute}

.top-bar{left:0;top:0;width:1200px;height:42px;background:var(--bar)}
.site-mark{left:87px;top:8px;width:26px;height:26px;background:#fff;border-radius:3px}
.search{left:122px;top:7px;width:444px;height:24px;background:#fff;border-radius:2px}
.search-btn{right:0;top:0;width:48px;height:24px;background:#f5f6f7;border-radius:0 2px 2px 0;display:flex;align-items:center;justify-content:center}
.user{left:763px;top:9px;display:flex;align-items:center;gap:6px;color:#fff;font-weight:600;font-size:12.5px;font-family:"Lato",sans-serif}
.user-thumb{width:22px;height:22px;background:#fff;display:flex;align-items:center;justify-content:center}
.user-thumb i{width:8px;height:8px;border-radius:50%;background:var(--navy)}
.bar-sep{width:1px;height:18px;background:rgba(255,255,255,.3);margin:0 6px}
.bar-icon{top:11px}

.profile-pic{left:90px;top:56px;width:166px;height:166px;background:#fff;border:1px solid var(--line);padding:3px}
.profile-inner{width:100%;height:100%;border:1px solid #ccc;display:flex;flex-direction:column;align-items:center;justify-content:center;gap:6px;text-align:center}
.brand-dot{width:44px;height:44px;border-radius:50%;background:var(--navy)}
.brand-name{font-family:"Noto Serif",serif;font-size:12px;color:#3a3a3a;line-height:1.3}
.brand-sub{font-family:"Noto Serif",serif;font-size:10.5px;color:#888}
.page-name{left:87px;top:236px;font-family:"Open Sans",sans-serif;font-size:25px;line-height:25px;color:#1d2129;letter-spacing:-.3px}
.page-handle{left:88px;top:293px;font-size:12.5px;color:#a88ca0}
.nav{left:87px;top:328px;width:175px}
.nav a{display:block;height:32px;line-height:32px;padding-left:10px;font-size:14px;color:var(--grey-text);text-decoration:none}
.nav a.active{background:#dddfe2;border-left:3px solid var(--bar);color:var(--ink);font-weight:600;padding-left:10px}

.cover-card{left:271px;top:43px;width:829px;height:365px;background:var(--card);border:1px solid var(--line)}
.cover{left:0;top:0;width:829px;height:315px;overflow:hidden;background:#fff}
.network{left:0;top:0;width:520px;height:315px;background:radial-gradient(circle at 30% 20%,#eef2f6 0,#fff 70%)}
.cover-brand{left:0;top:20px;width:413px;text-align:center}
.cover-brand .brand-dot{width:38px;height:38px;margin:0 auto 8px}
.cover-brand .brand-name{font-size:13px;color:#222}
.cover-brand .brand-sub{font-size:11px;color:#666;margin-top:2px}
.cover-title{left:0;top:109px;width:413px;text-align:center;font-family:"Montserrat",sans-serif;font-weight:500;font-size:24px;color:var(--navy)}
.cover-tagline{left:0;top:135px;width:413px;text-align:center;font-family:"Montserrat",sans-serif;font-weight:700;font-size:24px;color:var(--sky)}
.cover-intro{left:30px;top:172px;width:360px;text-align:center;font-family:"Montserrat",sans-serif;font-size:10px;line-height:15px;color:var(--navy)}
.services{left:0;top:226px;width:397px;height:51px;background:var(--navy-deep);border-radius:0 12px 12px 0;color:#fff;font-family:"Montserrat",sans-serif;font-weight:600;font-size:9.6px;line-height:13px;text-align:center;padding-top:6px}
.services span{margin:0 5px}
.cover-url{left:0;top:287px;width:413px;text-align:center;font-family:"Montserrat",sans-serif;font-size:13px;letter-spacing:2px;color:var(--navy)}
.cover-photo{left:413px;top:0;width:416px;height:315px;background:radial-gradient(ellipse at 58% 45%,#cfe3f3 0,#8fb6d8 45%,#c0472f 78%,#ffffff 100%);clip-path:ellipse(52% 50% at 56% 50%)}

.actions{left:12px;top:325px;display:flex;border:1px solid #ccd0d5;border-radius:2px;background:#f6f7f9}
.actions div{height:28px;padding:0 10px;display:flex;align-items:center;gap:5px;font-size:12px;font-weight:600;color:#4b4f56;border-right:1px solid #ccd0d5}
.actions div:last-child{border-right:0}
.contact-btn{left:516px;top:326px;width:298px;height:28px;background:var(--cta);color:#fff;font-size:14px;display:flex;align-items:center;justify-content:center;border-radius:2px}

.composer{left:271px;top:422px;width:502px;height:108px;background:var(--card);border:1px solid var(--line);border-radius:3px}
.composer-tabs{height:34px;background:#f6f7f9;border-bottom:1px solid var(--line);display:flex;align-items:center;gap:8px;padding-left:18px;font-size:12px;color:#4b4f56}
.composer-tabs .link{color:var(--bar)}
.composer-body{display:flex;align-items:center;gap:10px;padding:12px 14px;font-size:13.5px;color:#a88ca0}
.mini-thumb{width:38px;height:38px;border:1px solid var(--line);display:flex;align-items:center;justify-content:center}
.mini-thumb i{width:11px;height:11px;border-radius:50%;background:var(--navy)}

.likes-card{left:788px;top:421px;width:312px;height:108px;background:var(--card);border:1px solid var(--line);border-radius:3px}
.likes-row{display:flex;gap:12px;padding:12px 6px;border-bottom:1px solid var(--line);height:58px}
.likes-text{font-size:12.5px;line-height:19px;color:#4b4f56}
.likes-text .sub{color:#90949c}
.invite-row{display:flex;align-items:center;gap:22px;padding:12px 14px;font-size:12px;color:#4b4f56}
</style>
</head>
<body>
<header class="top-bar abs">
  <div class="site-mark abs"></div>
  <div class="search abs"><div class="search-btn abs">
    <svg width="13" height="13" viewBox="0 0 13 13"><circle cx="5.5" cy="5.5" r="4.3" fill="none" stroke="#4b4f56" stroke-width="1.5"/><line x1="8.7" y1="8.7" x2="12" y2="12" stroke="#4b4f56" stroke-width="1.5"/></svg>
  </div></div>
  <div class="user abs"><div class="user-thumb"><i></i></div>Dale Hersh<span class="bar-sep"></span>Home</div>
  <svg class="bar-icon abs" style="left:940px" width="22" height="18" viewBox="0 0 22 18" fill="#fff"><circle cx="7" cy="5" r="4"/><path d="M0 18c0-5 3-7 7-7s7 2 7 7z"/><circle cx="15" cy="4" r="3.4"/><path d="M13 10c4-1 9 1 9 8h-6z"/></svg>
  <svg class="bar-icon abs" style="left:974px" width="22" height="18" viewBox="0 0 22 18" fill="#fff"><path d="M0 1h14v9H5l-4 4v-4H0z"/><path d="M16 5h6v9h-2v4l-4-4H7v-2h9z"/></svg>
  <svg class="bar-icon abs" style="left:1008px" width="19" height="19" viewBox="0 0 20 20"><circle cx="10" cy="10" r="9.5" fill="#fff"/><path d="M5 4c2 1 3 3 2 5s2 3 3 6M12 2c0 3 3 3 5 4M13 12c2 0 3 2 4 3" stroke="var(--bar)" stroke-width="1.6" fill="none"/></svg>
  <svg class="bar-icon abs" style="left:1062px" width="40" height="16" viewBox="0 0 40 16" fill="#fff" opacity=".75"><rect x="1" y="6" width="12" height="9" rx="1"/><path d="M4 6V4a3 3 0 0 1 6 0v2" stroke="#fff" stroke-width="1.6" fill="none"/><path d="M26 5h10l-5 6z"/></svg>
</header>

<aside>
  <div class="profile-pic abs"><div class="profile-inner">
    <div class="brand-dot"></div>
    <div><div class="brand-name">Cargo Bridge Partners</div><div class="brand-sub">Transportation Brokers</div></div>
  </div></div>
  <h1 class="page-name abs">Cargo Bridge<br>Partners
    <svg width="20" height="20" viewBox="0 0 20 20" style="vertical-align:-3px"><circle cx="10" cy="10" r="10" fill="var(--verified)"/><path d="M5.5 10.3l3 3 6-6.3" stroke="#fff" stroke-width="2.2" fill="none"/></svg></h1>
  <div class="page-handle abs">@Cargo Bridge Partners</div>
  <nav class="nav abs">
    <a class="active">Home</a><a>Photos</a><a>Likes</a><a>About</a><a>Videos</a><a>Welcome</a><a>Posts</a>
  </nav>
</aside>

<section class="cover-card abs">
  <div class="cover abs">
    <div class="network abs"></div>
    <div class="cover-brand abs"><div class="brand-dot"></div><div class="brand-name">Cargo Bridge Partners</div><div class="brand-sub">Transportation Brokers</div></div>
    <div class="cover-title abs">Cargo Bridge Partners</div>
    <div class="cover-tagline abs">"WE LISTEN, WE DELIVER"</div>
    <p class="cover-intro abs">Cargo Bridge Partners is a full service Transportation Brokerage &amp; Freight Forwarder, we offer a full menu of transportation related options for our customer base:</p>
    <div class="services abs">
      <span>• FULL TRUCK LOAD SOLUTIONS</span><span>• LESS THAN TRUCK LOAD SOLUTIONS</span><br>
      <span>• RAIL RELATED SOLUTIONS</span><span>• AIR FREIGHT SOLUTIONS</span><br>
      <span>• SEA BASED SOLUTIONS</span><span>• WAREHOUSING &amp; STORAGE Solutions</span>
    </div>
    <div class="cover-url abs">www.vrnhtp.com</div>
    <div class="cover-photo abs" role="img" aria-label="Globe collage of a jet airliner over a city skyline, a container ship, a white truck with a container and a yellow freight locomotive"></div>
  </div>
  <div class="actions abs">
    <div><svg width="13" height="12" viewBox="0 0 13 12" fill="#4b66a5"><rect x="0" y="5" width="3" height="7"/><path d="M4 5l3-5c1.5 0 2 1 1.5 3H12c1 0 1 1 1 1.5L11.5 12H4z"/></svg>Liked ▾</div>
    <div><svg width="13" height="13" viewBox="0 0 13 13"><circle cx="6.5" cy="6" r="6" fill="#8d949e"/></svg>Message</div>
    <div>··· More ▾</div>
  </div>
  <div class="contact-btn abs">Contact Us</div>
</section>

<section class="composer abs">
  <div class="composer-tabs">
    <svg width="14" height="14" viewBox="0 0 14 14"><path d="M2 12l1-4 7-7 3 3-7 7z" fill="#4267b2"/></svg>Status
    <svg width="16" height="13" viewBox="0 0 16 13" style="margin-left:8px"><rect width="16" height="13" rx="2" fill="#8d949e"/><circle cx="8" cy="7" r="3" fill="#fff"/></svg><span class="link">Photo / Video</span>
  </div>
  <div class="composer-body"><div class="mini-thumb"><i></i></div>Write something on this Page...</div>
</section>

<section class="likes-card abs">
  <div class="likes-row"><div class="mini-thumb"><i></i></div>
    <div class="likes-text">1,955,550 people like this<br><span class="sub">Ray Colburn and 20 other friends</span></div></div>
  <div class="invite-row">
    <svg width="18" height="16" viewBox="0 0 18 16" fill="#bec3c9"><circle cx="7" cy="4.5" r="4"/><path d="M0 16c0-5 3-7 7-7s7 2 7 7z"/><path d="M14 2h1.5v2.5H18V6h-2.5v2.5H14V6h-2.5V4.5H14z"/></svg>
    Invite friends to like this Page</div>
</section>
</body>
</html>
```